Events Management Webpage

I am after a basic webpage for my events company Galorra based in Perth WA. It is a boutique events company that organises all kinds of events from corporate awards nights/gala balls, birthday celebrations, cocktail parties, quiz nights etc. I am wanting separate TABS for all of my services which are Corporate Events, Private Parties & Events, Venue Management, Wedding Planning, Event Design, My Desk Helper and of course a gallery and contact page. Galorra offers their services Australia wide if this can be made obvious on each of the pages.
The logo is quite pink - I do want Pink to be included on the page but I want the page to look sophisticated and designer not too girly and pink so that it appeals to all corporate markets mainly.
A small gallery or the ability to put in lots of pictures on each of the pages would be good as this is how people see my work.

Target Market(s)

Young event planners and Personal Assistants

Industry/Entity Type

Boutique

Requirements
Must have
• Separate TABS for each of my services.
A Contact Page
Nice to have
• Happy for designers to mess around with the logo and page colours.
Should not have
• I don't like the fonts to be too scripty and the colours too girly. I want the page to be stylish and modern and appeal to a high class market of corporate planners.

```html
<!DOCTYPE html>
<html lang="en">
<head>
<meta charset="utf-8">
<title>Galorra – Event &amp; Planning Services</title>
<link href="https://fonts.googleapis.com/css2?family=Didact+Gothic&family=Open+Sans:ital,wght@0,400;0,600;0,700;0,800;1,800&display=swap" rel="stylesheet">
<style>
:root{
  --pink:#a8135e;
  --ink:#332f30;
  --charcoal:#3a3738;
  --night:#231f20;
  --sand:#e6e2d8;
  --field:#8c8a8b;
  --grey:#bdbdbd;
  --white:#fff;
  --text:#555;
}
*{margin:0;padding:0;box-sizing:border-box}
html,body{width:961px;height:1200px;overflow:hidden;background:var(--white)}
body{position:relative;font-family:"Open Sans",sans-serif;color:var(--white)}
.abs{position:absolute}

/* header */
.brand{left:104px;top:100px;width:320px;text-align:center}
.brand-name{font-family:"Open Sans",sans-serif;font-weight:700;font-size:40px;color:var(--pink);line-height:1}
.brand-tag{font-family:"Didact Gothic",sans-serif;font-size:27px;color:var(--text);margin-top:8px;white-space:nowrap;text-align:left}
.call{left:693px;top:52px;width:163px;height:41px;background:#3d3b3c;box-shadow:1px 2px 3px rgba(0,0,0,.35);text-align:center;font-weight:600;font-size:13px;line-height:17px;padding-top:4px}
.social{left:750px;top:104px;display:flex;gap:13px}
.social span{width:26px;height:26px;border-radius:50%;background:var(--grey)}

/* navigation */
.nav{left:0;width:961px;height:49px;display:flex;justify-content:center}
.nav-top{top:198px;background:var(--pink)}
.nav-bottom{top:1151px;background:var(--night)}
.nav ul{list-style:none;display:flex;margin-left:-13px}
.nav li{font-family:"Didact Gothic",sans-serif;font-size:13px;line-height:12px;text-align:center;display:flex;align-items:center;justify-content:center;border-right:1px solid rgba(255,255,255,.35);height:49px;white-space:nowrap}
.nav-top li{border-right-color:rgba(0,0,0,.2)}
.nav li:last-child{border-right:0}

/* hero */
.hero-band{left:0;top:247px;width:961px;height:307px;background:#2e2b2c}
.hero{left:105px;top:250px;width:748px;height:304px;background:linear-gradient(180deg,#1d78b4 0%,#4ea3d4 42%,#1e6f9a 50%,#1aa1b6 70%,#36c3c8 100%)}
.hero-badge{left:112px;top:267px;width:170px;height:170px;background:var(--pink);opacity:.92;border-radius:50% 0 50% 50%}
.hero-badge p{position:absolute;left:6px;top:62px;width:160px;font-family:"Didact Gothic",sans-serif;font-size:24px;line-height:23px;text-align:center}
.hero-brand{left:690px;top:312px;width:140px;text-align:center}
.hero-brand b{display:block;font-weight:700;font-size:19px}
.hero-brand small{font-size:8.5px;white-space:nowrap}
.hero-title{left:105px;top:488px;width:748px;text-align:center;font-size:39px;letter-spacing:.5px;white-space:nowrap}
.hero-title b{font-weight:800}
.hero-title span{font-weight:400}
.hero-strip{left:0;top:554px;width:961px;height:8px;background:#444}

/* welcome */
.sand{left:0;top:562px;width:961px;height:349px;background:var(--sand)}
.dots{left:453px;top:568px;display:flex;gap:7px}
.dots span{width:10px;height:10px;border-radius:50%;background:var(--ink)}
.dots span:first-child{background:var(--white);border:1px solid var(--ink)}
.welcome{left:104px;top:590px;width:368px;height:287px;background:var(--ink)}
.welcome-tab{left:131px;top:562px;width:133px;height:102px}
.welcome-tab h2{position:absolute;left:0;top:32px;width:133px;text-align:center;font-weight:800;font-style:italic;font-size:25px}
.welcome-copy{left:127px;top:677px;width:335px;font-size:12.4px;line-height:14.4px}
.btn{background:var(--pink);color:var(--white);font-weight:700;font-size:13px;text-align:center;line-height:20px;height:20px;white-space:nowrap}
.photo{width:176px;height:137px}

/* lower */
.lower{left:0;top:911px;width:961px;height:240px;background:var(--charcoal)}
.tab{top:903px;height:34px;background:var(--pink);font-family:"Didact Gothic",sans-serif;font-size:18px;line-height:34px;padding-left:13px;white-space:nowrap}
.tab::after{content:"";position:absolute;right:-6px;top:0;border-left:6px solid var(--night);border-top:8px solid transparent}
.small{font-size:10.4px;line-height:12px}
.field{background:var(--field);font-weight:700;font-size:12px;padding-left:8px;line-height:22px}
.events{left:372px;top:966px;list-style:none;font-size:10.6px;white-space:nowrap}
.events li{height:19.3px;padding-left:12px;position:relative}
.events li::before{content:"";position:absolute;left:0;top:3px;width:5px;height:5px;background:var(--pink)}
</style>
</head>
<body>

<header>
  <div class="abs brand">
    <div class="brand-name">Galorra</div>
    <div class="brand-tag">Event &amp; Planning Services</div>
  </div>
  <div class="abs call">Call us now!<br><span style="font-size:14px">Tel: 1300 482 917</span></div>
  <div class="abs social" aria-label="Social links"><span></span><span></span><span></span></div>
</header>

<nav class="abs nav nav-top">
  <ul>
    <li style="width:90px">Corporate<br>Events</li>
    <li style="width:140px">Private Parties &amp;<br>Events</li>
    <li style="width:122px">Venue<br>Management</li>
    <li style="width:90px">Wedding<br>Planning</li>
    <li style="width:80px">Event<br>Design</li>
    <li style="width:82px">My Desk<br>Helper</li>
    <li style="width:72px">Gallery</li>
    <li style="width:80px">Contact</li>
  </ul>
</nav>

<section>
  <div class="abs hero-band"></div>
  <div class="abs hero" role="img" aria-label="Photo of a charter boat on turquoise water beside a small island"></div>
  <div class="abs hero-badge"><p>For unforgetable moments</p></div>
  <div class="abs hero-brand"><b>Galorra</b><small>Event &amp; Planning Services</small></div>
  <div class="abs hero-title"><b>ISLAND</b><span>DAY</span><b>OUT</b></div>
  <div class="abs hero-strip"></div>
</section>

<section>
  <div class="abs sand"></div>
  <div class="abs dots"><span></span><span></span><span></span><span></span></div>
  <div class="abs welcome"></div>
  <svg class="abs welcome-tab" viewBox="0 0 133 102" aria-hidden="true">
    <polygon points="0,0 133,0 133,55 66.5,102 0,55" fill="var(--pink)"/>
  </svg>
  <div class="abs welcome-tab"><h2>Welcome</h2></div>
  <p class="abs welcome-copy">Lorem Ipsum is simply dummy text of the printing and typesetting industry. Lorem Ipsum has been the industry's standard dummy text ever since the 1500s, when an unknown printer took a galley of type and scrambled. Lorem Ipsum is simply dummy text of the printing and typesetting industry. Lorem Ipsum has been the industry's standard dummy text ever since the 1500s, when an unknown printer took a galley of type and scrambled. Lorem Ipsum has been the industry's standard dummy text ever since the 1500s.</p>
  <div class="abs btn" style="left:368px;top:843px;width:89px">Learn More</div>

  <div class="abs photo" style="left:488px;top:590px;background:linear-gradient(135deg,#3a2a2a,#8c1b22 55%,#2b1c1c)" role="img" aria-label="Event photo: lounge with red drapes and dessert table"></div>
  <div class="abs photo" style="left:680px;top:590px;background:linear-gradient(135deg,#1d1a3a,#5a4fa8 50%,#a01a3a)" role="img" aria-label="Event photo: illuminated mirror arch over red carpet"></div>
  <div class="abs photo" style="left:488px;top:741px;background:linear-gradient(135deg,#2a1f3a,#121016 55%,#4a3a5a)" role="img" aria-label="Event photo: black dinner tables with candelabra"></div>
  <div class="abs photo" style="left:680px;top:741px;background:linear-gradient(135deg,#c76a6a,#8a7ab8 50%,#b13a3a)" role="img" aria-label="Event photo: banquet room with red chair covers"></div>
</section>

<section>
  <div class="abs lower"></div>

  <div class="abs tab" style="left:103px;width:109px">Newsletter</div>
  <p class="abs small" style="left:101px;top:966px;width:245px">Sign up here to receive regular e-newsletter. Please note you will only be added to the list if a full name is submitted.</p>
  <div class="abs field" style="left:101px;top:1023px;width:241px;height:28px;line-height:28px">Email</div>
  <div class="abs field" style="left:101px;top:1059px;width:241px;height:28px;line-height:28px">Name</div>
  <div class="abs btn" style="left:102px;top:1096px;width:89px">Submit</div>

  <div class="abs tab" style="left:360px;width:109px;padding-left:4px;font-size:17px">Latest Events</div>
  <ul class="abs events">
    <li>Sign up here to receive regular e-newsletter.</li>
    <li>Sign up here to receive regular e-newsletter.</li>
    <li>Sign up here to receive regular e-newsletter.</li>
    <li>Sign up here to receive regular e-newsletter.</li>
    <li>Sign up here to receive regular e-newsletter.</li>
    <li>Sign up here to receive regular e-newsletter.</li>
  </ul>
  <div class="abs btn" style="left:360px;top:1095px;width:88px">Learn More</div>

  <div class="abs tab" style="left:615px;width:109px;padding-left:10px">Contact Us</div>
  <div class="abs field" style="left:617px;top:969px;width:238px">Email</div>
  <div class="abs field" style="left:617px;top:997px;width:238px">Tel</div>
  <div class="abs field" style="left:617px;top:1026px;width:238px">Subject</div>
  <div class="abs field" style="left:617px;top:1056px;width:239px;height:52px">Contect</div>
  <div class="abs btn" style="left:617px;top:1118px;width:88px">Submit</div>
</section>

<nav class="abs nav nav-bottom">
  <ul>
    <li style="width:90px">Corporate<br>Events</li>
    <li style="width:142px">Private Parties &amp;<br>Events</li>
    <li style="width:119px">Venue<br>Management</li>
    <li style="width:91px">Wedding<br>Planning</li>
    <li style="width:81px">Event<br>Design</li>
    <li style="width:82px">My Desk<br>Helper</li>
    <li style="width:71px">Gallery</li>
    <li style="width:80px">Contact</li>
  </ul>
</nav>

</body>
</html>
```